Harbour Lensman's Atlas for iOS

I am a keen travel and lifestyle photographer whose photographic studio is Velmire Photographic, based in Sydney, Australia. You can see my photographic portfolio at velmirephotographic.com.

Overview
-
I want to create an iOS app that will allow Sydney-bound photographers to develop an understanding of some the popular and lesser known sights of this beautiful city and its surrounds. I’d like to achieve this by making available to serious photographers information that will allow them plan their photographic expeditions and explore their own creative interpretations of some classic Sydney photographs. Aiding more serious photographers, the Harbour Lensman’s Atlas will include photographic metadata that most other photo sites exclude, allowing photographers to explore their own settings and creative options with guidance from scene-specific shooting data (Exposure and ISO settings, natural lighting and time of day, focal length etc).

The functionality of the iOS app I’d like to develop are:

1) Ability to review a thumbnail list of Sydney-based photographic galleries (Presented in a “Scenes” tab which the user starts with on launching the app).

a. A section at the bottom will include a “Sydney’s Surrounds” section which will be separated from the other Scenes by some kind of delimiter ( “………..” etc or something more stylish). Under this delimeter will be scenes from surround areas – including “The Hunter Valley”, “The Central Coast”, “The Blue Mountains”, “Woollongong”.

b. At the very bottom of app will be a “Link to Velmire Photographic by Tomas Ferrow” which will link to the URL for my site.

2) Ability to select each ‘scene’ and be presented with a gallery of photograph thumbnails from this scene (Presented in a “Gallery” tab which is opened once a Scene is selected from within the “Scenes” tab by touching on that scene’s thumbnail or its associated brief). Note: You can use the “Gallery” drop down menu from my web site for a sense of how I’d like this to look.

3) Having selected a photograph’s thumbnail from the Gallery tab, a user is then taken to an “Image” screen that presents the photograph itself.

a. Within the Image screen, there will be an option to touch an “Info” button, selection of which will trigger the appearance of a semi-opaque overlay tile will appear with the following information:

i. Focal length:
ii. ISO:
iii. F-stop:
iv. Time:
v. Post-production:
vi. A general description field where information is provided around how the photograph was conceived and composed.

b. Within the Image screen, there also be a “Location” button”. On selecting “Location” the user will be taken to a “Map” screen that will present an iOS Maps screen with a pin showing the location the photograph was taken.

c. Finally, within the Image screen, there also be a “Favourite” button”. On selecting “Favourite” the user will ‘star’ the photo and it will be added to the Favourites screen accessed through the Favourites tab (see below)

4) Users will be presented with a fourth tab that will present the “Map” screen. It will be accessed by selecting the “Location” button from within the Image screen, or by directly pressing on the Maps tab itself. There will be Icon which if selected will pinpoint the user’s current location in relation to the photograph’s location (if one has been selected).

5) A “Favourites” screen will be accessed from a fifth Tab that will allow users to see a gallery of all their favourite photographs’ thumbnails.

General Navigation and Look and Feel
-
• I would like a clean and uncluttered modern design that takes guidance from the general look and feel of my website (velmirephotographic.com).
• The UI should be iPad and iPhone friendly. Note: The iPad version would be an expanded resolution of the iPhone version (ie. not relying on a 2x expansion but not necessarily requiring a whole new UI).

I'm looking forward to developing this concept further with your design involvement.
Updates

Hello

I have doubled the committed budget on this design.  Looking forward to your entries.  
Tomas

I do like the idea of a black backgrounded app.  This is the style of my site velmirephotographic.com and blends well into the photo styles used.  It is well presented in the initial design submitted.

Target Market(s)

Serious amateur and semi-pro photographers.

Industry/Entity Type

Travel

Requirements
Must have
• - Galleries that are tiled vertically. You can use the gearlodge app and its list of articles for a view of how this can be presented.

Basically, I'd like

Picture - brief description

You can get a sense of these by looking at my Gallery drop down menu from my website.

- The app needs to look like an app for pro users, and serious photographers. It's not intended to be gimicky, but look professional and elegant.
Should not have
• Not use old style fonts. I would like them clean and modern and economical.

```html
<!DOCTYPE html>
<html lang="en">
<head>
<meta charset="utf-8">
<title>Harbour Lensman's Atlas – app screens</title>
<link href="https://fonts.googleapis.com/css2?family=Bebas+Neue&family=Open+Sans:wght@400;600&display=swap" rel="stylesheet">
<style>
  :root {
    --page-bg: #ececec;
    --screen-bg: #050505;
    --bar-top: #3a3a3a;
    --bar-bottom: #1c1c1c;
    --rule: #3b3b3b;
    --title: #ffffff;
    --muted: #7c7c7c;
    --tab-bg: #2a2a2a;
    --tab-active: #3c3c3c;
    --tab-label: #e8e8e8;
    --frame: #8f8f8f;
    --photo-light: #d9e48a;
    --photo-mid: #8fae5f;
    --photo-dark: #3d5a3a;
    --overlay: rgba(255,255,255,0.55);
    --stat-box: rgba(90,90,90,0.55);
    --overlay-text: #3a3a3a;
  }
  * { box-sizing: border-box; margin: 0; padding: 0; }
  html, body { width: 1200px; height: 536px; overflow: hidden; }
  body { background: var(--page-bg); position: relative; font-family: 'Open Sans', Arial, sans-serif; }

  .screen {
    position: absolute; top: 44px; width: 286px; height: 432px;
    background: var(--screen-bg); overflow: hidden;
    box-shadow: 0 2px 6px rgba(0,0,0,0.25);
  }
  .screen--list { left: 114px; }
  .screen--photo { left: 441px; }
  .screen--info { left: 763px; }

  .top-bar {
    height: 39px;
    background: linear-gradient(var(--bar-top), var(--bar-bottom));
    border-bottom: 1px solid #555;
  }

  /* scene list */
  .scene-list { list-style: none; padding: 0 4px; }
  .scene-row {
    display: flex; height: 60px; padding: 16px 0 0 6px;
    border-bottom: 1px solid var(--rule);
  }
  .scene-row:first-child { padding-top: 16px; height: 73px; }
  .thumb {
    flex: none; width: 46px; height: 46px; margin-right: 5px;
    border: 2px solid #b9b9a4;
    background: linear-gradient(var(--photo-light), var(--photo-mid) 60%, var(--photo-dark));
  }
  .scene-title { font-family: 'Bebas Neue', sans-serif; font-size: 16px; color: var(--title); line-height: 16px; margin-top: 1px; }
  .scene-brief { font-size: 8.6px; color: var(--muted); line-height: 12px; margin-top: 3px; }

  /* photo view */
  .photo-frame {
    position: absolute; left: 13px; top: 75px; width: 260px; height: 258px;
    background: var(--frame); padding: 7px 7px 9px;
  }
  .photo {
    width: 100%; height: 100%;
    background: linear-gradient(#e4ec9a 0%, #b6c06a 12%, #6f7a45 20%, #c9d98a 32%, #9dbb6c 55%, #5c8357 80%, #3e6446 100%);
  }
  .action-bar { position: absolute; top: 338px; left: 12px; right: 12px; height: 19px; }
  .action {
    position: absolute; top: 0; height: 19px; display: flex; align-items: center;
    font-family: 'Bebas Neue', sans-serif; font-size: 10px; color: var(--tab-label);
    background: #1d1d1d; border-left: 3px solid #777; border-right: 3px solid #777; padding: 1px 6px 0;
  }
  .action--info { left: 0; width: 165px; }
  .action--locate { right: 0; width: 56px; justify-content: space-between; }
  .action svg { fill: var(--tab-label); }

  /* info overlay */
  .info-panel {
    position: absolute; left: 12px; top: 75px; width: 167px; height: 282px;
    background: var(--overlay); padding: 8px 7px;
  }
  .stats {
    background: var(--stat-box); padding: 4px 6px 3px;
    font-family: 'Bebas Neue', sans-serif; font-size: 11px; line-height: 15px; color: #f2f2f2;
    width: 148px;
  }
  .stats dt { display: inline; }
  .stats dd { display: inline; color: #cfcfcf; }
  .info-text { font-size: 8.6px; line-height: 12.6px; color: var(--overlay-text); margin-top: 13px; padding: 0 4px; }

  /* tab bar */
  .tab-bar {
    position: absolute; left: 0; bottom: 0; width: 100%; height: 48px;
    display: flex; align-items: flex-end; background: #111;
  }
  .tab {
    height: 44px; display: flex; flex-direction: column; align-items: center; justify-content: flex-end;
    padding-bottom: 5px; border-radius: 4px 4px 0 0;
    background: linear-gradient(#3b3b3b, var(--tab-bg));
    font-family: 'Bebas Neue', sans-serif; font-size: 10px; color: var(--tab-label);
  }
  .tab svg { width: 24px; height: 22px; fill: #e6e6e6; margin-bottom: 3px; }
  .tab--site { width: 64px; }
  .tab--favorite { width: 81px; height: 48px; background: linear-gradient(#4a4a4a, var(--tab-active) 30%, #2c2c2c); box-shadow: 0 0 4px #000; }
  .tab--near { width: 66px; }
  .tab--gallery { width: 75px; }
</style>
</head>
<body>
<svg width="0" height="0" style="position:absolute" aria-hidden="true">
  <defs>
    <symbol id="icon-home" viewBox="0 0 24 22"><path d="M12 1 1 11h3v10h6v-6h4v6h6V11h3z"/></symbol>
    <symbol id="icon-star" viewBox="0 0 24 22"><path d="M12 0l3.2 7.4 8 .7-6 5.3 1.8 7.9L12 17.2 5 21.3l1.8-7.9-6-5.3 8-.7z"/></symbol>
    <symbol id="icon-target" viewBox="0 0 24 22"><path fill-rule="evenodd" d="M12 0a11 11 0 1 1 0 22 11 11 0 0 1 0-22zm0 4a7 7 0 1 0 0 14 7 7 0 0 0 0-14z"/><path d="M13 7l2 1-3 5-2-1z"/></symbol>
    <symbol id="icon-camera" viewBox="0 0 24 22"><path fill-rule="evenodd" d="M1 5h6l2-3h6l2 3h6v15H1zm11 3a5 5 0 1 0 0 10 5 5 0 0 0 0-10zm0 2.5a2.5 2.5 0 1 1 0 5 2.5 2.5 0 0 1 0-5z"/></symbol>
    <symbol id="icon-pin" viewBox="0 0 8 14"><circle cx="4" cy="4" r="3.5"/><rect x="3.3" y="6" width="1.4" height="8"/></symbol>
    <symbol id="icon-play" viewBox="0 0 6 8"><path d="M0 0l6 4-6 4z"/></symbol>
  </defs>
</svg>

<!-- Scenes list -->
<section class="screen screen--list">
  <header class="top-bar"></header>
  <ul class="scene-list">
    <li class="scene-row"><div class="thumb" role="img" aria-label="Thumbnail: figure standing in a lake at dusk"></div><div><h2 class="scene-title">Paris</h2><p class="scene-brief">Lorem ipsum dolor sit amet, consectetur adipiscing elit. Mauris iaculis hendrerit nibh in consequat. Cras</p></div></li>
    <li class="scene-row"><div class="thumb" role="img" aria-label="Thumbnail: figure standing in a lake at dusk"></div><div><h2 class="scene-title">New York City</h2><p class="scene-brief">Lorem ipsum dolor</p></div></li>
    <li class="scene-row"><div class="thumb" role="img" aria-label="Thumbnail: figure standing in a lake at dusk"></div><div><h2 class="scene-title">Paris</h2><p class="scene-brief">Lorem ipsum dolor sit amet, consectetur adipiscing elit. Mauris iaculis hendrerit nibh in consequat. Cras</p></div></li>
    <li class="scene-row"><div class="thumb" role="img" aria-label="Thumbnail: figure standing in a lake at dusk"></div><div><h2 class="scene-title">New York City</h2><p class="scene-brief">Lorem ipsum dolor</p></div></li>
    <li class="scene-row"><div class="thumb" role="img" aria-label="Thumbnail: figure standing in a lake at dusk"></div><div><h2 class="scene-title">Paris</h2><p class="scene-brief">Lorem ipsum dolor sit amet, consectetur adipiscing elit. Mauris iaculis hendrerit nibh in consequat. Cras</p></div></li>
    <li class="scene-row"><div class="thumb" role="img" aria-label="Thumbnail: figure standing in a lake at dusk"></div><div><h2 class="scene-title">New York City</h2><p class="scene-brief">Lorem ipsum dolor</p></div></li>
  </ul>
  <nav class="tab-bar">
    <div class="tab tab--site"><svg><use href="#icon-home"/></svg>Site</div>
    <div class="tab tab--favorite"><svg><use href="#icon-star"/></svg>Favorite</div>
    <div class="tab tab--near"><svg><use href="#icon-target"/></svg>Near Me</div>
    <div class="tab tab--gallery"><svg><use href="#icon-camera"/></svg>Gallery</div>
  </nav>
</section>

<!-- Image screen -->
<section class="screen screen--photo">
  <header class="top-bar"></header>
  <div class="photo-frame"><div class="photo" role="img" aria-label="Photograph: a woman wading in a calm green lake under a hazy sky"></div></div>
  <div class="action-bar">
    <div class="action action--info">Photo Infos&nbsp;&nbsp;<svg width="6" height="8"><use href="#icon-play"/></svg></div>
    <div class="action action--locate"><svg width="8" height="14"><use href="#icon-pin"/></svg>Locate</div>
  </div>
  <nav class="tab-bar">
    <div class="tab tab--site"><svg><use href="#icon-home"/></svg>Site</div>
    <div class="tab tab--favorite"><svg><use href="#icon-star"/></svg>Favorite</div>
    <div class="tab tab--near"><svg><use href="#icon-target"/></svg>Near Me</div>
    <div class="tab tab--gallery"><svg><use href="#icon-camera"/></svg>Gallery</div>
  </nav>
</section>

<!-- Image screen with info overlay -->
<section class="screen screen--info">
  <header class="top-bar"></header>
  <div class="photo-frame"><div class="photo" role="img" aria-label="Photograph: a woman wading in a calm green lake under a hazy sky"></div></div>
  <div class="action-bar">
    <div class="action action--info">Photo Infos&nbsp;&nbsp;<svg width="6" height="8"><use href="#icon-play"/></svg></div>
    <div class="action action--locate"><svg width="8" height="14"><use href="#icon-pin"/></svg>Locate</div>
  </div>
  <aside class="info-panel">
    <dl class="stats">
      <dt>ISO:</dt> <dd>100</dd><br>
      <dt>Focal Lenght:</dt> <dd>50mm</dd><br>
      <dt>Exposure:</dt> <dd>F 4,5</dd>
    </dl>
    <p class="info-text">Lorem ipsum dolor sit amet, consectetur adipiscing elit. Nullam vel odio et felis dignissim suscipit eu nec dolor. Nam tristique elit dapibus magna viverra ut sagittis libero sodales. Pellentesque habitant morbi tristique senectus et netus et malesuada fames ac turpis egestas. Nulla velit dolor, tristique vel euismod.</p>
  </aside>
  <nav class="tab-bar">
    <div class="tab tab--site"><svg><use href="#icon-home"/></svg>Site</div>
    <div class="tab tab--favorite"><svg><use href="#icon-star"/></svg>Favorite</div>
    <div class="tab tab--near"><svg><use href="#icon-target"/></svg>Near Me</div>
    <div class="tab tab--gallery"><svg><use href="#icon-camera"/></svg>Gallery</div>
  </nav>
</section>
</body>
</html>
```